Brightmere Glowworks - Two Pages of Information and Pictures

We need a two page summary of the Service Offerings of Brightmere Glowworks - a company that installs LED Lighting. We've written the copy and picked images and chart that we like and have laid it out a word document.

We're looking for someone to design a more professional page layout than the generic Word Template. Please do not feel the current layout is suggested. It is only laid out this way because Word had that template. Be as creative as you want.

We would like the images and text to be in the same order that it is in now.

We're also in a rush so speed is appreciated. THANK YOU !!

Target Market(s)

Corporate Offices in New York

Industry/Entity Type

Lighting Fixture

Colors
85cae6
87cfc7
9bcb3c
3377b5

Requirements
Must have
• Must include two pages of the copy and images written and provided in the word document that was uploaded. Must use the Brightmere colors in the logo.
Nice to have
• An easy to read flow of images and.

```html
<!DOCTYPE html>
<html lang="en">
<head>
<meta charset="utf-8">
<title>Brightmere Glowworks – Service Overview</title>
<link rel="stylesheet" href="https://fonts.googleapis.com/css2?family=Baloo+2:wght@600;700&family=Didact+Gothic&family=Open+Sans:wght@400;600&display=swap">
<style>
:root{
  --sky:#85cae6;
  --teal:#87cfc7;
  --green:#9bcb3c;
  --blue:#3377b5;
  --ink:#2b2b2b;
  --charcoal:#2a2a2a;
  --paper:#f3f3f4;
  --stage:#e6e6e8;
}
*{box-sizing:border-box;margin:0;padding:0}
html,body{width:1200px;height:1200px;overflow:hidden;background:var(--stage)}
.canvas{position:relative;width:1200px;height:1200px}
.page{position:absolute;top:240px;width:560px;height:720px;background:var(--paper);overflow:hidden;box-shadow:0 4px 14px rgba(0,0,0,.18)}
.page--front{left:27px}
.page--back{left:613px;background:#f7f7f7}

/* front */
.front-top{position:absolute;left:0;top:0;width:560px;height:160px;background:#f1f1f3}
.deco{position:absolute;display:block}
.brand{position:absolute;top:38px;left:0;width:560px;text-align:center}
.brand__name{display:inline-flex;align-items:center;gap:9px;font-family:"Didact Gothic",sans-serif;font-size:27px;letter-spacing:3px;color:#3f7a64}
.brand__mark{width:14px;height:14px;background:var(--teal)}
.brand__tagline{position:absolute;top:120px;width:560px;text-align:center;font-family:"Didact Gothic",sans-serif;font-size:15px;color:#333}
.photo{position:absolute;top:160px;height:283px}
.photo--bulbs{left:0;width:190px;background:linear-gradient(160deg,#4a3a2a,#b88a4a 55%,#3a2e24);clip-path:polygon(0 0,100% 0,93% 100%,0 100%)}
.photo--office{left:178px;width:215px;background:linear-gradient(170deg,#e9ecee,#c9cfd2 55%,#8a8f93);clip-path:polygon(7% 0,100% 0,93% 100%,0 100%)}
.photo--lounge{left:380px;width:180px;background:linear-gradient(165deg,#2d2a28,#9a7046 50%,#d9cfc4);clip-path:polygon(7% 0,100% 0,100% 100%,0 100%)}
.front-lower{position:absolute;top:443px;left:0;width:560px;height:246px;background:linear-gradient(180deg,#eeeeef,#f4f4f5)}
.headline{position:absolute;top:490px;width:560px;text-align:center;font-family:"Baloo 2",sans-serif;font-weight:700;font-size:52px;line-height:1;color:var(--blue)}
.headline__accent{color:var(--green)}
.offer{position:absolute;left:29px;top:602px;width:502px;height:81px;border:1px solid var(--blue);padding:13px 6px 0}
.offer__tab{position:absolute;top:-17px;left:50%;transform:translateX(-50%);background:#3a3a3a;color:#fff;font-family:"Open Sans",sans-serif;font-weight:600;font-size:13px;padding:4px 10px;white-space:nowrap}
.offer__text{font-family:"Open Sans",sans-serif;font-size:9.3px;line-height:1.27;text-align:justify;color:#222}

/* footer */
.footer{position:absolute;left:0;bottom:0;width:560px;height:31px}
.footer svg{position:absolute;inset:0}
.footer__item{position:absolute;top:0;height:31px;display:flex;align-items:center;gap:6px;font-family:"Didact Gothic",sans-serif;font-size:10.5px;white-space:nowrap}
.footer__item--phone{left:30px;color:#1e3a12}
.footer__item--mail{left:165px;color:#fff}
.footer__item--web{left:372px;color:#fff}

/* back */
.banner{position:absolute;left:0;top:0;width:560px;height:111px;background:linear-gradient(180deg,#8fd3cb,var(--teal))}
.banner__skyline{position:absolute;left:0;bottom:0;width:560px;height:95px;background:linear-gradient(180deg,rgba(120,190,182,0),rgba(95,170,162,.7))}
.banner__title{position:absolute;top:42px;left:195px;width:170px;height:30px;border:1.5px solid #fff;display:flex;align-items:center;justify-content:center;font-family:"Baloo 2",sans-serif;font-weight:600;font-size:16px;color:#fff;white-space:nowrap}
.label{position:absolute;border:1px solid var(--green);padding:1px 4px;font-family:"Baloo 2",sans-serif;font-weight:600;font-size:10.5px;line-height:1.2;color:var(--green);letter-spacing:.3px;background:#f7f7f7}
.label--dark{border-color:#222;color:#111;background:transparent}
.body{position:absolute;font-family:"Didact Gothic",sans-serif;font-size:8.6px;line-height:1.25;color:#222;text-align:justify}
.body p+p{margin-top:5px}
.why{left:30px;top:145px;width:224px}
.why-wide{left:30px;top:300px;width:500px}
.chart{position:absolute;left:268px;top:128px;width:264px;height:175px}
.chart__title{font-family:"Open Sans",sans-serif;font-size:8.5px;color:#333;text-align:center}
.team-backdrop{position:absolute;left:36px;top:350px;width:170px;height:112px;background:var(--teal);transform:rotate(-3deg)}
.team-photo{position:absolute;left:28px;top:358px;width:170px;height:112px;background:linear-gradient(175deg,#5f7a3a,#6b8fc3 55%,#3c5477)}
.team-text{left:232px;top:375px;width:298px}
.testimonials{position:absolute;left:0;top:498px;width:560px;height:164px;background:var(--sky)}
.quotes{position:absolute;left:30px;top:37px;width:500px;font-family:"Didact Gothic",sans-serif;font-size:8.6px;line-height:1.23;color:#1c1c1c}
.quote+.quote{margin-top:6px}
.quote__source{display:block;font-family:"Open Sans",sans-serif;font-style:italic;font-weight:600;color:#fff}
</style>
</head>
<body>
<main class="canvas">

  <section class="page page--front" aria-label="Front page">
    <div class="front-top">
      <svg class="deco" style="left:0;top:0" width="560" height="160" viewBox="0 0 560 160" aria-hidden="true">
        <polygon points="0,0 70,0 110,30 10,150 0,150" fill="#85cae6" opacity=".35"/>
        <polygon points="10,5 85,20 60,110 -10,95" fill="#85cae6" opacity=".3"/>
        <polygon points="560,85 560,160 500,160" fill="#85cae6" opacity=".4"/>
        <polygon points="540,100 560,125 560,160 515,160" fill="#85cae6" opacity=".3"/>
      </svg>
      <div class="brand"><span class="brand__name"><span class="brand__mark"></span>BRIGHTMERE</span></div>
      <p class="brand__tagline">Making LEDs beautiful.</p>
    </div>

    <div class="photo photo--bulbs" role="img" aria-label="Photo of warm Edison filament bulbs hanging on brass pendants"></div>
    <div class="photo photo--office" role="img" aria-label="Photo of a bright open-plan office with desks and monitors"></div>
    <div class="photo photo--lounge" role="img" aria-label="Photo of a lounge with track lighting, wood panels and white chairs"></div>

    <div class="front-lower"></div>
    <h1 class="headline">Making LEDs <span class="headline__accent">Beautiful</span></h1>

    <div class="offer">
      <span class="offer__tab">No Upfront Cost – Turnkey LEDs</span>
      <p class="offer__text">Brightmere Glowworks provides LED lighting as a service – fully implemented and managed LEDs at no upfront cost. Brightmere takes the risk, hassle and capital cost out of adopting LED's energy saving technology. Brightmere guarantees net-savings for customers on day one, and continues to guarantee savings and performance for the full term of the contract. And the savings add up! A project can be installed 2-4 weeks from kickoff, and projects continue to generate savings for up to 10 years.</p>
    </div>

    <footer class="footer">
      <svg width="560" height="31" viewBox="0 0 560 31" aria-hidden="true">
        <rect width="560" height="31" fill="#9bcb3c"/>
        <polygon points="160,0 364,0 356,31 152,31" fill="#2a2a2a"/>
        <polygon points="155,0 160,0 152,31 147,31" fill="#fff"/>
        <polygon points="364,0 369,0 361,31 356,31" fill="#fff"/>
      </svg>
      <span class="footer__item footer__item--phone">
        <svg width="11" height="11" viewBox="0 0 24 24" aria-hidden="true"><path d="M6.6 10.8a15 15 0 0 0 6.6 6.6l2.2-2.2a1 1 0 0 1 1-.25 11.4 11.4 0 0 0 3.6.57 1 1 0 0 1 1 1V20a1 1 0 0 1-1 1A17 17 0 0 1 3 4a1 1 0 0 1 1-1h3.5a1 1 0 0 1 1 1c0 1.25.2 2.45.57 3.6a1 1 0 0 1-.25 1z" fill="#fff"/></svg>
        347 555 GLOW</span>
      <span class="footer__item footer__item--mail">
        <svg width="11" height="11" viewBox="0 0 12 12" aria-hidden="true"><circle cx="6" cy="6" r="6" fill="#9bcb3c"/><rect x="3" y="4" width="6" height="4" fill="none" stroke="#2a2a2a" stroke-width="1"/></svg>
        customers@brightmereglowworks.com</span>
      <span class="footer__item footer__item--web">
        <svg width="11" height="11" viewBox="0 0 12 12" aria-hidden="true"><circle cx="6" cy="6" r="5.3" fill="none" stroke="#fff" stroke-width="1.2"/><ellipse cx="6" cy="6" rx="2.2" ry="5.3" fill="none" stroke="#fff"/><line x1="1" y1="6" x2="11" y2="6" stroke="#fff"/></svg>
        www.brightmereglowworks.com</span>
    </footer>
  </section>

  <section class="page page--back" aria-label="Back page">
    <div class="banner">
      <div class="banner__skyline" role="img" aria-label="Tinted photo of the New York skyline with a suspension bridge"></div>
      <h2 class="banner__title">Brightmere Glowworks</h2>
    </div>

    <h3 class="label" style="left:30px;top:128px">WHY USE BRIGHTMERE?</h3>
    <div class="body why">
      <p>Brightmere's customers understand the value of LEDs but don't want to deal with the risk, hassle and capital cost on their own. Brightmere starts saving customers money the first month – typically a net-savings of about 4.7 cents a square-foot per month. Brightmere will design aesthetic LED systems and install the best available technology.</p>
      <p>Brightmere provides LEDs at the best cost with its as-a-service structure, which puts the cost of lighting into clients' monthly operating budget for less than they save. By installing projects immediately, Brightmere eliminates the cost of foregone savings that would accumulate from delayed implementation.</p>
    </div>

    <figure class="chart">
      <figcaption class="chart__title">Annual and Total Net-Savings of 250,000 ft2 Customer</figcaption>
      <svg width="264" height="162" viewBox="0 0 264 162" role="img" aria-label="Bar and line chart of annual service cost, annual net-savings and total net-savings over ten years">
        <g font-family="Open Sans, sans-serif" font-size="4.5" fill="#555">
          <text x="2" y="40" transform="rotate(-90 5 40)">Thousands</text>
          <text x="258" y="28" transform="rotate(90 258 28)">Millions</text>
          <g text-anchor="end">
            <text x="26" y="12">$300</text><text x="26" y="35">$250</text><text x="26" y="57">$200</text>
            <text x="26" y="80">$150</text><text x="26" y="102">$100</text><text x="26" y="125">$50</text><text x="26" y="147">$-</text>
          </g>
          <g>
            <text x="238" y="12">$2.0</text><text x="238" y="26">$1.8</text><text x="238" y="39">$1.6</text><text x="238" y="53">$1.4</text>
            <text x="238" y="66">$1.2</text><text x="238" y="80">$1.0</text><text x="238" y="93">$0.8</text><text x="238" y="107">$0.6</text>
            <text x="238" y="120">$0.4</text><text x="238" y="134">$0.2</text><text x="238" y="147">$0.0</text>
          </g>
        </g>
        <g stroke="#e2e2e2" stroke-width=".5">
          <line x1="30" y1="10" x2="232" y2="10"/><line x1="30" y1="33" x2="232" y2="33"/><line x1="30" y1="55" x2="232" y2="55"/>
          <line x1="30" y1="78" x2="232" y2="78"/><line x1="30" y1="100" x2="232" y2="100"/><line x1="30" y1="123" x2="232" y2="123"/>
        </g>
        <line x1="30" y1="145" x2="232" y2="145" stroke="#bbb" stroke-width=".6"/>
        <g fill="#a9d6ec">
          <rect x="33" y="104" width="6" height="41"/><rect x="53" y="104" width="6" height="41"/><rect x="73" y="104" width="6" height="41"/>
          <rect x="93" y="104" width="6" height="41"/><rect x="113" y="104" width="6" height="41"/>
        </g>
        <g fill="#8cbf5a">
          <rect x="40" y="82" width="6" height="63"/><rect x="60" y="82" width="6" height="63"/><rect x="80" y="82" width="6" height="63"/>
          <rect x="100" y="82" width="6" height="63"/><rect x="120" y="82" width="6" height="63"/>
          <rect x="140" y="38" width="6" height="107"/><rect x="160" y="38" width="6" height="107"/><rect x="180" y="38" width="6" height="107"/>
          <rect x="200" y="38" width="6" height="107"/><rect x="220" y="38" width="6" height="107"/>
        </g>
        <polyline points="40,140 60,131 80,121 100,112 120,102 140,87 160,72 180,58 200,43 220,28 228,20" fill="none" stroke="#666" stroke-width=".8"/>
        <g font-family="Open Sans, sans-serif" font-size="4.5" fill="#555" text-anchor="middle">
          <text x="40" y="153">1</text><text x="60" y="153">2</text><text x="80" y="153">3</text><text x="100" y="153">4</text><text x="120" y="153">5</text>
          <text x="140" y="153">6</text><text x="160" y="153">7</text><text x="180" y="153">8</text><text x="200" y="153">9</text><text x="220" y="153">10</text>
        </g>
        <g font-family="Open Sans, sans-serif" font-size="3.8" fill="#555">
          <rect x="48" y="157" width="8" height="2.5" fill="#a9d6ec"/><text x="58" y="160">Annual Brightmere Service</text>
          <rect x="118" y="157" width="8" height="2.5" fill="#8cbf5a"/><text x="128" y="160">Annual Net-Savings</text>
          <line x1="172" y1="158" x2="180" y2="158" stroke="#666" stroke-width=".8"/><text x="182" y="160">Total Net-Savings</text>
        </g>
      </svg>
    </figure>

    <div class="body why-wide">
      <p>It can be risky to adopt new technology, especially when salespeople try to sell more than is needed. Brightmere has access to better equipment and at better cost than is widely available on the open market and passes that quality and savings on to its customers. Brightmere guarantees performance for 5 years, which removes the risk of a failed project.</p>
    </div>

    <div class="team-backdrop"></div>
    <div class="team-photo" role="img" aria-label="Photo of the team in matching blue t-shirts seen from behind, standing in a garden"></div>

    <h3 class="label" style="left:232px;top:353px">THE BEST TEAM IN LEDS</h3>
    <div class="body team-text">
      <p>Brightmere is a team of lighting experts who get the evolution of lighting and efficiency. Simply put, we come in up every day with one goal: to provide an excellent service that saves money and uses less electricity. Part of the team focuses on the supply chain of the very best equipment that customers have come to appreciate. Part of the team focuses on the project management of each installation. And, part of the team focuses on resolving any questions customers might have in their transition. Together we make up the best team in LEDs and work tirelessly to make it easy to upgrade.</p>
    </div>

    <section class="testimonials">
      <h3 class="label label--dark" style="left:30px;top:12px">TESTIMONIALS</h3>
      <div class="quotes">
        <blockquote class="quote">"Brightmere made a huge improvement in the lighting for our headquarters. The installation process was as smooth as can be and the service since has been excellent."<span class="quote__source">– Harborline Health</span></blockquote>
        <blockquote class="quote">"In a museum, quality lighting is paramount. Brightmere has been a great partner in helping us transition to LEDs that look great, save us money, and make lighting management so much simpler."<span class="quote__source">– Little Makers Art Museum, New York</span></blockquote>
        <blockquote class="quote">"We are so happy to have had Brightmere's help building out our new office space – they put their lighting expertise to work delivering beautiful LEDs and fixtures. It was cost-effective, removed lighting from the build-out budget, and it's been a joy to work with them since."<span class="quote__source">– Fieldgrain Works, Inc</span></blockquote>
      </div>
    </section>

    <footer class="footer">
      <svg width="560" height="31" viewBox="0 0 560 31" aria-hidden="true">
        <rect width="560" height="31" fill="#9bcb3c"/>
        <polygon points="160,0 364,0 356,31 152,31" fill="#2a2a2a"/>
        <polygon points="155,0 160,0 152,31 147,31" fill="#fff"/>
        <polygon points="364,0 369,0 361,31 356,31" fill="#fff"/>
      </svg>
      <span class="footer__item footer__item--phone">
        <svg width="11" height="11" viewBox="0 0 24 24" aria-hidden="true"><path d="M6.6 10.8a15 15 0 0 0 6.6 6.6l2.2-2.2a1 1 0 0 1 1-.25 11.4 11.4 0 0 0 3.6.57 1 1 0 0 1 1 1V20a1 1 0 0 1-1 1A17 17 0 0 1 3 4a1 1 0 0 1 1-1h3.5a1 1 0 0 1 1 1c0 1.25.2 2.45.57 3.6a1 1 0 0 1-.25 1z" fill="#fff"/></svg>
        347 555 GLOW</span>
      <span class="footer__item footer__item--mail">
        <svg width="11" height="11" viewBox="0 0 12 12" aria-hidden="true"><circle cx="6" cy="6" r="6" fill="#9bcb3c"/><rect x="3" y="4" width="6" height="4" fill="none" stroke="#2a2a2a" stroke-width="1"/></svg>
        customers@brightmereglowworks.com</span>
      <span class="footer__item footer__item--web">
        <svg width="11" height="11" viewBox="0 0 12 12" aria-hidden="true"><circle cx="6" cy="6" r="5.3" fill="none" stroke="#fff" stroke-width="1.2"/><ellipse cx="6" cy="6" rx="2.2" ry="5.3" fill="none" stroke="#fff"/><line x1="1" y1="6" x2="11" y2="6" stroke="#fff"/></svg>
        www.brightmereglowworks.com</span>
    </footer>
  </section>

</main>
</body>
</html>
```